Full Service Outdoor Property Management Company

We are looking for a new and fresh business card design. My company has been in business for 26 years. Winter: We are a large snow and ice management company that does work for commercial, industrial and municipal clients. We have been named "Top 100 Snow Companies in the U.S." for numerous years. Summer: We provide complete landscape maintenance and landscape design and construction for both residential and commercial clients. We must incorporate our logo into card design as well as (in no particular order):
Employees name
Office: (417) 803-2765
Cell: (xxx) xxx-xxxx
brightfold.com
1879 Marigold, Ashford MI 49210
(Something about 26 + years in business as well as "Top 100 snow contractors as stated above)
Target Market(s)
Winter: Commercial, Industrial, Municipal
Summer: Residential and Commercial
Industry/Entity Type
Construction
Contact Information for Business Card
This is a little challenging as we are using one card for essentially two companies that target different customers from summer to winter. Perhaps the back side could be split in two or something to highlight the different services?? I'm open to any ideas!! Looking forward to seeing what you come up with!
Requirements
Must have
- Logo
- (in no particular order)
- Employees name
- Office: (417) 803-2765
- Cell: (xxx) xxx-xxxx
- brightfold.com
- 1879 Marigold, Ashford MI 49210
Nice to have
- Something about 26 + years in business
- "Top 100 Snow Contractors in the U.S."
Should not have
- Cheesy pictures of lawn mowers and snow plows

```html
<!DOCTYPE html>
<html lang="en">
<head>
<meta charset="utf-8">
<title>Brightfold Business Card</title>
<link href="https://fonts.googleapis.com/css2?family=Arimo:wght@400;700&display=swap" rel="stylesheet">
<style>
  :root {
    --page: #ecebe8;
    --card: #fbfbfb;
    --card-edge: #e4e4e4;
    --green: #0b8a4a;
    --green-dark: #07703b;
    --ink: #555555;
    --rule: #d9d9d9;
    --icon: #2aa7d8;
    --band-rule: #4d4d4d;
  }
  * { box-sizing: border-box; margin: 0; padding: 0; }
  html, body {
    width: 1200px; height: 1023px; overflow: hidden;
    background: var(--page);
    font-family: "Arimo", Arial, sans-serif;
  }
  .canvas { position: relative; width: 1200px; height: 1023px; }
  .card {
    position: absolute; width: 560px; height: 320px;
    background: linear-gradient(135deg, #ffffff 0%, var(--card) 60%, #f1f1f1 100%);
    border: 1px solid var(--card-edge);
    box-shadow: 0 6px 18px rgba(0,0,0,0.12);
    overflow: hidden;
  }
  /* Front */
  .card-front { left: 70px; top: 90px; }
  .brand {
    position: absolute; left: 0; top: 0; width: 300px; height: 320px;
    display: flex; align-items: center; justify-content: center; gap: 12px;
  }
  .brand-mark { width: 18px; height: 18px; background: var(--green); }
  .brand-name { font-size: 40px; font-weight: 400; color: var(--green); letter-spacing: 0.5px; }
  .divider {
    position: absolute; left: 300px; top: 20px; width: 1px; height: 280px;
    background: linear-gradient(to bottom, transparent, var(--rule) 20%, var(--rule) 80%, transparent);
  }
  .contact { position: absolute; left: 330px; top: 62px; color: var(--ink); }
  .person-name { font-size: 21px; font-weight: 700; color: var(--green); margin-bottom: 12px; }
  .contact-line { font-size: 14px; line-height: 21px; letter-spacing: 0.8px; }
  .contact-group { position: relative; }
  .contact-icons {
    position: absolute; left: -26px; top: 3px;
    display: flex; flex-direction: column; gap: 8px;
  }
  .icon-chip { width: 13px; height: 13px; border-radius: 2px; background: var(--icon); }
  .address { margin-top: 36px; position: relative; }
  .address .pin { position: absolute; left: -26px; top: 3px; }
  /* Back */
  .card-back { left: 570px; top: 600px; }
  .backdrop-art {
    position: absolute; left: 0; bottom: 0; width: 170px; height: 120px;
    background: radial-gradient(circle at 30% 60%, #e2e2e2 0%, rgba(240,240,240,0) 70%);
  }
  .backdrop-snow {
    position: absolute; right: 0; top: 0; width: 200px; height: 110px;
    background: radial-gradient(circle at 70% 40%, #e6e6e6 0%, rgba(240,240,240,0) 70%);
  }
  .service { position: absolute; color: var(--ink); font-size: 15px; line-height: 21px; text-align: center; width: 100%; }
  .service-winter { top: 50px; }
  .service-summer { bottom: 46px; }
  .band {
    position: absolute; left: 0; width: 100%; top: 116px; height: 70px;
    background: linear-gradient(to bottom, var(--green), var(--green-dark));
    color: #ffffff; text-align: center; padding-top: 14px;
  }
  .band-rule { position: absolute; left: 0; width: 100%; height: 4px; top: 186px; background: var(--band-rule); }
  .band-years { font-size: 15px; font-weight: 700; line-height: 20px; }
  .band-claim { font-size: 16px; line-height: 22px; }
  .band-claim strong { font-weight: 700; }
</style>
</head>
<body>
<div class="canvas">
  <section class="card card-front">
    <div class="brand">
      <span class="brand-mark"></span>
      <span class="brand-name">Brightfold</span>
    </div>
    <div class="divider"></div>
    <div class="contact">
      <p class="person-name">Daniel Porter</p>
      <div class="contact-group">
        <div class="contact-icons">
          <span class="icon-chip"></span><span class="icon-chip"></span><span class="icon-chip"></span>
        </div>
        <p class="contact-line">(417) 803-2765</p>
        <p class="contact-line">(xxx) xxx-xxxx</p>
        <p class="contact-line">brightfold.com</p>
      </div>
      <div class="address">
        <svg class="pin" width="13" height="13" viewBox="0 0 13 13" aria-hidden="true">
          <rect width="13" height="13" rx="2" fill="#2aa7d8"/>
          <path d="M6.5 2.5a2.6 2.6 0 0 0-2.6 2.6c0 2 2.6 5.2 2.6 5.2s2.6-3.2 2.6-5.2a2.6 2.6 0 0 0-2.6-2.6z" fill="#fff"/>
          <circle cx="6.5" cy="5.1" r="0.9" fill="#2aa7d8"/>
        </svg>
        <p class="contact-line">1879 Marigold,</p>
        <p class="contact-line">Ashford MI 49210</p>
      </div>
    </div>
  </section>

  <section class="card card-back">
    <div class="backdrop-art" role="img" aria-label="Faint dandelion seed head decoration"></div>
    <div class="backdrop-snow" role="img" aria-label="Faint snowflake decoration"></div>
    <div class="service service-winter">
      <p>Winter:</p>
      <p>Commercial, Industrial, Municipal</p>
    </div>
    <div class="band">
      <p class="band-years">26 Years</p>
      <p class="band-claim">Top <strong>100</strong> Snow Contractors in the U.S.</p>
    </div>
    <div class="band-rule"></div>
    <div class="service service-summer">
      <p>Summer:</p>
      <p>Residential &amp; Commercial</p>
    </div>
  </section>
</div>
</body>
</html>
```